Design Shopify E-Commerce Website for Men's Products

Design a Shopify website for men to sell our men's jewelry, cigar and bar accessories, and other men's products. Design should be hip, with like a rock n' roll, biker, whiskey driker flare. Name of the company is "Ironvale Locker" and website will be www.IronvaleLocker.com
Homepage will have navigation bar with three categories: Men's Jewelry, Cigar & Bar Products, Man Cave Swag
I will upload our logo, inspiration type pictures and some of the products that we sell
Theme colors should be mainly dark: black, grey, brown, gold

```html
<!DOCTYPE html>
<html lang="en">
<head>
<meta charset="utf-8">
<title>Ironvale Locker</title>
<link href="https://fonts.googleapis.com/css2?family=Bebas+Neue&family=Montserrat:wght@400;500;600&display=swap" rel="stylesheet">
<style>
:root{
  --black:#0b0b0b;
  --ink:#1a1a1a;
  --grey:#6d6d6d;
  --light:#f1f1f1;
  --gold:#b89b5e;
  --gold-hi:#d8c28d;
  --gold-lo:#6b5529;
  --white:#ffffff;
}
*{margin:0;padding:0;box-sizing:border-box}
html,body{width:1200px;height:4312px;overflow:hidden;background:var(--white)}
body{position:relative;font-family:"Montserrat",sans-serif;color:var(--ink)}
.abs{position:absolute}
.display{font-family:"Bebas Neue",sans-serif;font-weight:400}
.gold-btn{position:absolute;display:flex;align-items:center;justify-content:center;gap:14px;
  background:linear-gradient(90deg,var(--gold-hi),var(--gold) 50%,var(--gold-lo));
  color:var(--white);font-family:"Bebas Neue",sans-serif;letter-spacing:7px;font-size:24px}
.arrow{width:28px;height:12px}
.promo{left:0;top:0;width:1200px;height:28px;background:var(--black);color:var(--white);font-size:11px;
  display:flex;align-items:center;justify-content:center}
.promo b{color:var(--gold);font-weight:500;margin-right:4px}
.nav{left:0;top:28px;width:1200px;height:98px;background:var(--white)}
.nav a{position:absolute;top:44px;font-size:13px;letter-spacing:1px;color:#333;text-decoration:none}
.brand-mark{left:520px;top:36px;width:160px;height:140px;background:var(--black);border-radius:0 0 80px 80px;
  display:flex;flex-direction:column;align-items:center;justify-content:center;gap:8px;z-index:3}
.brand-mark .dot{width:34px;height:34px;border-radius:50%;background:var(--gold)}
.brand-mark span{color:var(--gold);font-weight:600;font-size:15px;letter-spacing:1px}
.hero{left:0;top:126px;width:1200px;height:524px;background:radial-gradient(ellipse at 72% 50%,#8a8a8a,#3a3a3a 45%,#0d0d0d 85%)}
.hero h1{position:absolute;left:118px;top:150px;color:var(--white);font-size:92px;line-height:86px;letter-spacing:26px}
.tile{position:absolute;display:flex;flex-direction:column;align-items:center;justify-content:flex-end;color:var(--white)}
.tile h3{font-size:32px;letter-spacing:5px}
.section-title{position:absolute;width:1200px;text-align:center;font-size:40px;letter-spacing:6px;color:var(--black)}
.card{position:absolute;top:1426px;width:223px}
.card .img{width:223px;height:273px}
.card .name{margin-top:20px;font-size:15px;font-weight:500}
.stars{display:flex;gap:3px;margin-top:6px}
.stars svg{width:13px;height:13px}
.card .row{display:flex;justify-content:space-between;align-items:center;margin-top:12px}
.price{font-size:15px;font-weight:500}
.cart-btn{width:112px;height:28px;border:1px solid #bbb;display:flex;align-items:center;justify-content:center;gap:12px;
  font-family:"Bebas Neue",sans-serif;font-size:12px;letter-spacing:2px;color:var(--gold)}
.body-text{font-size:13.5px;line-height:22px;color:#333}
.news-field{position:absolute;border-bottom:1px solid #999;font-size:13px;color:#333;padding-bottom:12px}
.feature{position:absolute;top:3775px;display:flex;gap:14px;align-items:center}
.feature h4{font-family:"Bebas Neue",sans-serif;font-weight:400;font-size:22px;letter-spacing:1px}
.feature p{font-size:12.5px;color:#888}
.feature svg{width:58px;height:42px}
.footer{left:0;top:3872px;width:1200px;height:440px;background:var(--black);color:#aaa}
.foot-col{position:absolute;top:80px}
.foot-col h5{font-family:"Bebas Neue",sans-serif;font-weight:400;font-size:22px;letter-spacing:2px;color:var(--white);margin-bottom:24px}
.foot-col li{list-style:none;font-size:13px;margin-bottom:15px}
</style>
</head>
<body>

<div class="abs promo"><b>15% OFF</b> ON YOUR FIRST ORDER</div>

<nav class="abs nav">
  <a style="left:120px">HOME</a><a style="left:205px">ABOUT US</a><a style="left:320px">SHOP</a>
  <a style="left:788px">FAQ'S</a><a style="left:864px">CONTACT</a>
  <svg class="abs" style="left:964px;top:38px" width="22" height="22" viewBox="0 0 22 22" fill="none" stroke="#222" stroke-width="1.8"><circle cx="9" cy="9" r="7"/><path d="M14 14l6 6"/></svg>
  <svg class="abs" style="left:1012px;top:38px" width="20" height="22" viewBox="0 0 20 22" fill="none" stroke="#222" stroke-width="1.8"><circle cx="10" cy="7" r="5"/><path d="M2 21c0-5 4-8 8-8s8 3 8 8"/></svg>
  <svg class="abs" style="left:1060px;top:38px" width="24" height="24" viewBox="0 0 24 24" fill="none" stroke="#222" stroke-width="1.8"><path d="M3 7h14l-1 14H4z"/><path d="M7 7V5a3 3 0 016 0v2"/><circle cx="19" cy="19" r="3" fill="#b89b5e" stroke="none"/></svg>
</nav>

<div class="abs brand-mark"><div class="dot"></div><span>Ironvale Locker</span></div>

<section class="abs hero" role="img" aria-label="Black and white close-up of chrome motorcycles">
  <h1 class="display">Ironvale<br>Locker</h1>
  <div class="gold-btn" style="left:118px;top:354px;width:208px;height:54px">SHOP NOW
    <svg class="arrow" viewBox="0 0 28 12" fill="none" stroke="#fff" stroke-width="1.6"><path d="M0 6h26M21 1l5 5-5 5"/></svg></div>
</section>

<div class="tile" style="left:20px;top:670px;width:569px;height:281px;padding-bottom:26px;background:radial-gradient(ellipse at 55% 40%,#4d5a63,#222a30 55%,#101214)" role="img" aria-label="Ornate silver ring with a dark gemstone on rough stone">
  <h3 class="display">Men's Jewellery</h3></div>
<div class="tile" style="left:20px;top:971px;width:569px;height:281px;padding-bottom:26px;background:radial-gradient(ellipse at 45% 40%,#a0582a,#5a2e15 55%,#25130a)" role="img" aria-label="Open cigar humidor with whiskey glass and cutter">
  <h3 class="display">Cigar &amp; Bar Products</h3></div>
<div class="tile" style="left:609px;top:670px;width:570px;height:582px;padding-bottom:64px;background:linear-gradient(180deg,#8a5a35,#6b3f24 45%,#3a2214 80%,#1d110a)" role="img" aria-label="Wood-panelled man cave with leather sofa and globe bar">
  <h3 class="display">Man Cave Swag</h3>
  <p style="font-size:15px;font-weight:500;margin:10px 0 24px">Discover unbeatable deals on all your man essentials</p>
  <div class="gold-btn" style="position:relative;width:208px;height:54px">SHOP NOW
    <svg class="arrow" viewBox="0 0 28 12" fill="none" stroke="#fff" stroke-width="1.6"><path d="M0 6h26M21 1l5 5-5 5"/></svg></div>
</div>

<h2 class="section-title display" style="top:1346px">Featured Products</h2>
<svg class="abs" style="left:72px;top:1578px" width="28" height="12" viewBox="0 0 28 12" fill="none" stroke="#222" stroke-width="1.6"><path d="M28 6H2M7 1L2 6l5 5"/></svg>
<svg class="abs" style="left:1100px;top:1578px" width="28" height="12" viewBox="0 0 28 12" fill="none" stroke="#222" stroke-width="1.6"><path d="M0 6h26M21 1l5 5-5 5"/></svg>

<div class="card" style="left:120px"><div class="img" style="background:linear-gradient(160deg,#9a8a74,#5d5245 60%,#3d352d)" role="img" aria-label="Pair of silver cufflinks on weathered wood"></div>
  <p class="name">Lorem ipsum - sit amet</p>
  <div class="stars"><svg viewBox="0 0 10 10"><path d="M5 0l1.5 3.3 3.5.4-2.6 2.4.7 3.5L5 7.8 1.9 9.6l.7-3.5L0 3.7l3.5-.4z" fill="#a8874a"/></svg><svg viewBox="0 0 10 10"><path d="M5 0l1.5 3.3 3.5.4-2.6 2.4.7 3.5L5 7.8 1.9 9.6l.7-3.5L0 3.7l3.5-.4z" fill="#a8874a"/></svg><svg viewBox="0 0 10 10"><path d="M5 0l1.5 3.3 3.5.4-2.6 2.4.7 3.5L5 7.8 1.9 9.6l.7-3.5L0 3.7l3.5-.4z" fill="#a8874a"/></svg><svg viewBox="0 0 10 10"><path d="M5 0l1.5 3.3 3.5.4-2.6 2.4.7 3.5L5 7.8 1.9 9.6l.7-3.5L0 3.7l3.5-.4z" fill="#a8874a"/></svg><svg viewBox="0 0 10 10"><path d="M5 0l1.5 3.3 3.5.4-2.6 2.4.7 3.5L5 7.8 1.9 9.6l.7-3.5L0 3.7l3.5-.4z" fill="#a8874a"/></svg></div>
  <div class="row"><span class="price">$ 59,99</span><span class="cart-btn">Add to cart <svg width="20" height="10" viewBox="0 0 28 12" fill="none" stroke="#333" stroke-width="1.6"><path d="M0 6h26M21 1l5 5-5 5"/></svg></span></div></div>

<div class="card" style="left:365px"><div class="img" style="background:radial-gradient(ellipse at 50% 55%,#8c8c8c,#3f3f3f 55%,#1e1e1e)" role="img" aria-label="Braided leather bracelet with silver skull charm"></div>
  <p class="name">Lorem ipsum - sit amet</p>
  <div class="stars"><svg viewBox="0 0 10 10"><path d="M5 0l1.5 3.3 3.5.4-2.6 2.4.7 3.5L5 7.8 1.9 9.6l.7-3.5L0 3.7l3.5-.4z" fill="#a8874a"/></svg><svg viewBox="0 0 10 10"><path d="M5 0l1.5 3.3 3.5.4-2.6 2.4.7 3.5L5 7.8 1.9 9.6l.7-3.5L0 3.7l3.5-.4z" fill="#a8874a"/></svg><svg viewBox="0 0 10 10"><path d="M5 0l1.5 3.3 3.5.4-2.6 2.4.7 3.5L5 7.8 1.9 9.6l.7-3.5L0 3.7l3.5-.4z" fill="#a8874a"/></svg><svg viewBox="0 0 10 10"><path d="M5 0l1.5 3.3 3.5.4-2.6 2.4.7 3.5L5 7.8 1.9 9.6l.7-3.5L0 3.7l3.5-.4z" fill="#a8874a"/></svg><svg viewBox="0 0 10 10"><path d="M5 0l1.5 3.3 3.5.4-2.6 2.4.7 3.5L5 7.8 1.9 9.6l.7-3.5L0 3.7l3.5-.4z" fill="#a8874a"/></svg></div>
  <div class="row"><span class="price">$ 59,99</span><span class="cart-btn">Add to cart <svg width="20" height="10" viewBox="0 0 28 12" fill="none" stroke="#333" stroke-width="1.6"><path d="M0 6h26M21 1l5 5-5 5"/></svg></span></div></div>

<div class="card" style="left:611px"><div class="img" style="background:linear-gradient(170deg,#6b4423,#b07a45 50%,#5a3519)" role="img" aria-label="Wooden cigar boxes stacked on shelves"></div>
  <p class="name">Lorem ipsum - sit amet</p>
  <div class="stars"><svg viewBox="0 0 10 10"><path d="M5 0l1.5 3.3 3.5.4-2.6 2.4.7 3.5L5 7.8 1.9 9.6l.7-3.5L0 3.7l3.5-.4z" fill="#a8874a"/></svg><svg viewBox="0 0 10 10"><path d="M5 0l1.5 3.3 3.5.4-2.6 2.4.7 3.5L5 7.8 1.9 9.6l.7-3.5L0 3.7l3.5-.4z" fill="#a8874a"/></svg><svg viewBox="0 0 10 10"><path d="M5 0l1.5 3.3 3.5.4-2.6 2.4.7 3.5L5 7.8 1.9 9.6l.7-3.5L0 3.7l3.5-.4z" fill="#a8874a"/></svg><svg viewBox="0 0 10 10"><path d="M5 0l1.5 3.3 3.5.4-2.6 2.4.7 3.5L5 7.8 1.9 9.6l.7-3.5L0 3.7l3.5-.4z" fill="#a8874a"/></svg><svg viewBox="0 0 10 10"><path d="M5 0l1.5 3.3 3.5.4-2.6 2.4.7 3.5L5 7.8 1.9 9.6l.7-3.5L0 3.7l3.5-.4z" fill="#a8874a"/></svg></div>
  <div class="row"><span class="price">$ 59,99</span><span class="cart-btn">Add to cart <svg width="20" height="10" viewBox="0 0 28 12" fill="none" stroke="#333" stroke-width="1.6"><path d="M0 6h26M21 1l5 5-5 5"/></svg></span></div></div>

<div class="card" style="left:855px"><div class="img" style="background:radial-gradient(ellipse at 50% 60%,#7a4a28,#2e2a27 60%,#1e1e1e)" role="img" aria-label="Wooden table-top cigar cutter with chrome handle"></div>
  <p class="name">Lorem ipsum - sit amet</p>
  <div class="stars"><svg viewBox="0 0 10 10"><path d="M5 0l1.5 3.3 3.5.4-2.6 2.4.7 3.5L5 7.8 1.9 9.6l.7-3.5L0 3.7l3.5-.4z" fill="#a8874a"/></svg><svg viewBox="0 0 10 10"><path d="M5 0l1.5 3.3 3.5.4-2.6 2.4.7 3.5L5 7.8 1.9 9.6l.7-3.5L0 3.7l3.5-.4z" fill="#a8874a"/></svg><svg viewBox="0 0 10 10"><path d="M5 0l1.5 3.3 3.5.4-2.6 2.4.7 3.5L5 7.8 1.9 9.6l.7-3.5L0 3.7l3.5-.4z" fill="#a8874a"/></svg><svg viewBox="0 0 10 10"><path d="M5 0l1.5 3.3 3.5.4-2.6 2.4.7 3.5L5 7.8 1.9 9.6l.7-3.5L0 3.7l3.5-.4z" fill="#a8874a"/></svg><svg viewBox="0 0 10 10"><path d="M5 0l1.5 3.3 3.5.4-2.6 2.4.7 3.5L5 7.8 1.9 9.6l.7-3.5L0 3.7l3.5-.4z" fill="#a8874a"/></svg></div>
  <div class="row"><span class="price">$ 59,99</span><span class="cart-btn">Add to cart <svg width="20" height="10" viewBox="0 0 28 12" fill="none" stroke="#333" stroke-width="1.6"><path d="M0 6h26M21 1l5 5-5 5"/></svg></span></div></div>

<div class="gold-btn" style="left:467px;top:1848px;width:265px;height:55px">ALL PRODUCTS
  <svg class="arrow" viewBox="0 0 28 12" fill="none" stroke="#fff" stroke-width="1.6"><path d="M0 6h26M21 1l5 5-5 5"/></svg></div>

<section class="abs" style="left:0;top:1980px;width:1200px;height:513px;background:linear-gradient(90deg,#050505 30%,#2a1a10 55%,#6b4226 80%,#3a2416)" role="img" aria-label="Cigars resting on a wooden box in warm low light">
  <h2 class="display abs" style="left:120px;top:98px;font-size:40px;letter-spacing:6px;color:var(--white)">View New Arrivals</h2>
  <p class="abs" style="left:120px;top:154px;font-size:13.5px;color:#ddd">Ut enim ad minima veniam, quis nostrum exercitationem</p>
  <div class="abs" style="left:120px;top:196px;width:105px;height:2px;background:linear-gradient(90deg,#fff,transparent)"></div>
  <h3 class="abs" style="left:120px;top:232px;font-size:20px;font-weight:500;color:var(--white)">Lorem ipsum - sit amet</h3>
  <p class="abs" style="left:120px;top:270px;width:400px;font-size:12.5px;line-height:21px;color:#ccc">Sed ut perspiciatis unde omnis iste natus error sit voluptatem accusantium doloremque laudantium, totam rem aperiam, eaque ipsa quae ab illo inventore veritatis.</p>
  <span class="abs" style="left:120px;top:364px;font-size:15px;font-weight:500;color:var(--white)">$ 59,99</span>
  <span class="abs cart-btn" style="left:229px;top:357px;border-color:#ccc;color:#ddd">Add to cart <svg width="20" height="10" viewBox="0 0 28 12" fill="none" stroke="#ddd" stroke-width="1.6"><path d="M0 6h26M21 1l5 5-5 5"/></svg></span>
  <div class="abs" style="left:120px;top:470px;width:46px;height:2px;background:#666"></div>
  <div class="abs" style="left:175px;top:470px;width:46px;height:2px;background:#fff"></div>
  <div class="abs" style="left:230px;top:470px;width:46px;height:2px;background:#666"></div>
  <div class="abs" style="left:285px;top:470px;width:46px;height:2px;background:#666"></div>
</section>

<div class="abs" style="left:120px;top:2595px;width:421px;height:477px;background:linear-gradient(135deg,#5a4a3d,#2e2520 55%,#14100d)" role="img" aria-label="Silver chain necklace with cross pendant over a leather jacket"></div>
<h2 class="display abs" style="left:616px;top:2620px;font-size:40px;letter-spacing:6px">About Us</h2>
<div class="abs" style="left:616px;top:2666px;width:110px;height:2px;background:linear-gradient(90deg,var(--gold),transparent)"></div>
<p class="abs body-text" style="left:616px;top:2690px;width:430px">Sed ut perspiciatis unde omnis iste natus error sit voluptatem accusantium doloremque laudantium, totam rem aperiam, eaque ipsa quae ab illo inventore veritatis et quasi architecto beatae vitae dicta sunt explicabo.</p>
<p class="abs body-text" style="left:616px;top:2800px;width:430px">Nemo enim ipsam voluptatem quia voluptas sit aspernatur aut odit aut fugit, sed quia consequuntur magni dolores eos qui ratione voluptatem sequi nesciunt. Neque porro quisquam est, qui dolorem ipsum quia dolor sit amet, consectetur, adipisci velit, sed quia non numquam eius modi tempora incidunt ut labore et dolore magnam aliquam quaerat voluptatem.</p>
<p class="abs body-text" style="left:120px;top:3122px;width:450px">Ut enim ad minima veniam, quis nostrum exercitationem ullam corporis suscipit laboriosam, nisi ut aliquid ex ea commodi consequatur? Quis autem vel eum iure reprehenderit qui in ea voluptate velit esse quam nihil molestiae consequatur, vel illum qui dolorem eum fugiat quo voluptas nulla pariatur</p>
<div class="abs" style="left:616px;top:2986px;width:462px;height:335px;background:radial-gradient(ellipse at 50% 50%,#6e625a,#3a332f 55%,#1f1b19)" role="img" aria-label="Braided leather bracelet with silver cross charm"></div>

<section class="abs" style="left:0;top:3408px;width:1200px;height:315px;background:var(--light)">
  <h2 class="display abs" style="left:120px;top:110px;font-size:40px;letter-spacing:5px">Subscribe Our Newsletter</h2>
  <p class="abs" style="left:120px;top:166px;font-size:13.5px">Ut enim ad minima veniam, quis nostrum exercitationem</p>
  <div class="news-field" style="left:625px;top:90px;width:185px">First Name</div>
  <div class="news-field" style="left:853px;top:90px;width:185px">First Name</div>
  <div class="news-field" style="left:625px;top:144px;width:413px">Email Address</div>
  <div class="gold-btn" style="left:624px;top:208px;width:217px;height:55px">SUBSCRIBE
    <svg class="arrow" viewBox="0 0 28 12" fill="none" stroke="#fff" stroke-width="1.6"><path d="M0 6h26M21 1l5 5-5 5"/></svg></div>
</section>

<div class="feature" style="left:118px"><svg viewBox="0 0 58 42" fill="none" stroke="#b89b5e" stroke-width="1.6"><path d="M12 10h26v20H12zM38 16h9l6 7v7H38"/><circle cx="20" cy="32" r="4"/><circle cx="45" cy="32" r="4"/><path d="M2 18h8M4 24h6"/></svg><div><h4>Free Delivery</h4><p>For all orders over $159</p></div></div>
<div class="abs" style="left:343px;top:3770px;width:1px;height:50px;background:#ddd"></div>
<div class="feature" style="left:392px"><svg viewBox="0 0 58 42" fill="none" stroke="#b89b5e" stroke-width="1.6"><rect x="12" y="9" width="34" height="24" rx="2"/><path d="M12 16h34M17 26h10"/></svg><div><h4>Secure Payment</h4><p>100% secure payment</p></div></div>
<div class="abs" style="left:618px;top:3770px;width:1px;height:50px;background:#ddd"></div>
<div class="feature" style="left:642px"><svg viewBox="0 0 58 42" fill="none" stroke="#b89b5e" stroke-width="1.6"><path d="M15 24v-6a14 14 0 0128 0v6"/><rect x="11" y="22" width="7" height="11" rx="2"/><rect x="40" y="22" width="7" height="11" rx="2"/><path d="M43 33c0 4-5 6-12 6"/></svg><div><h4>24/7 Support</h4><p>Dedicated support</p></div></div>
<div class="abs" style="left:862px;top:3770px;width:1px;height:50px;background:#ddd"></div>
<div class="feature" style="left:880px"><svg viewBox="0 0 58 42" fill="none" stroke="#b89b5e" stroke-width="1.6"><rect x="13" y="14" width="32" height="8"/><rect x="16" y="22" width="26" height="18"/><path d="M29 14v26M29 14c-4-8-12-6-8-1M29 14c4-8 12-6 8-1"/></svg><div><h4>Gift Service</h4><p>Support gift service</p></div></div>

<footer class="abs footer">
  <div class="abs" style="left:120px;top:80px;width:140px;display:flex;flex-direction:column;align-items:center;gap:10px">
    <div style="width:40px;height:40px;border-radius:50%;background:var(--gold)"></div>
    <span style="color:var(--gold);font-weight:600;font-size:15px">Ironvale Locker</span>
  </div>
  <h5 class="display abs" style="left:142px;top:236px;font-size:22px;letter-spacing:2px;color:var(--white)">Social Media</h5>
  <div class="abs" style="left:133px;top:274px;display:flex;gap:11px">
    <span style="width:20px;height:20px;border-radius:50%;border:1px solid #888"></span>
    <span style="width:20px;height:20px;border-radius:50%;background:var(--gold)"></span>
    <span style="width:20px;height:20px;border-radius:50%;border:1px solid #888"></span>
    <span style="width:20px;height:20px;border-radius:50%;border:1px solid #888"></span>
  </div>
  <div class="foot-col" style="left:354px"><h5>Quick Links</h5><ul><li>Home</li><li>About Us</li><li>Shop</li><li>Faq's</li><li>Contact</li></ul></div>
  <div class="foot-col" style="left:504px"><h5>Get Help</h5><ul><li>Help Center</li><li>Track Order</li><li>Returns</li><li>Privacy Policy</li><li>Terms of Service</li></ul></div>
  <div class="foot-col" style="left:675px"><h5>Shop Now</h5><ul><li>Men's Jewellery</li><li>Cigar &amp; Bar Products</li><li>Man Cave Swag</li></ul></div>
  <div class="foot-col" style="left:877px"><h5>Contact Info</h5>
    <p style="color:var(--white);font-size:14px;display:flex;gap:6px;align-items:center"><svg width="12" height="14" viewBox="0 0 12 14"><path d="M6 0a5 5 0 015 5c0 4-5 9-5 9S1 9 1 5a5 5 0 015-5z" fill="#b89b5e"/><circle cx="6" cy="5" r="2" fill="#0b0b0b"/></svg>Visit Us:</p>
    <p style="font-size:12.5px;line-height:18px;margin-top:4px">418 Forge Lane, Millbrook,<br>Ohio 44021</p>
    <p style="color:var(--white);font-size:14px;display:flex;gap:6px;align-items:center;margin-top:16px"><svg width="13" height="13" viewBox="0 0 13 13"><path d="M3 0l2 3-1.5 1.5a8 8 0 005 5L10 8l3 2-1.5 3C6 13 0 7 0 1.5z" fill="#b89b5e"/></svg>Phone:</p>
    <p style="font-size:12.5px;margin-top:6px">(555) 014-2286</p>
    <p style="color:var(--white);font-size:14px;display:flex;gap:6px;align-items:center;margin-top:18px"><svg width="14" height="11" viewBox="0 0 14 11" fill="#b89b5e"><rect width="14" height="11" rx="1"/><path d="M0 1l7 5 7-5" stroke="#0b0b0b" fill="none"/></svg>Email:</p>
    <p style="font-size:12.5px;margin-top:6px">info@ironvalelocker.com</p>
  </div>
  <div class="abs" style="left:120px;top:368px;width:958px;height:1px;background:#333"></div>
  <p class="abs" style="left:120px;top:394px;font-size:12px">© 2023 All Rights Reserved | <b style="color:var(--white);font-weight:600">IRONVALE LOCKER</b></p>
  <div class="abs" style="left:813px;top:390px;display:flex;gap:5px">
    <span style="width:34px;height:21px;border-radius:3px;background:#1a3a8c"></span>
    <span style="width:34px;height:21px;border-radius:3px;background:#e8e8e8"></span>
    <span style="width:34px;height:21px;border-radius:3px;background:#e8e8e8"></span>
    <span style="width:34px;height:21px;border-radius:3px;background:#5e9ed6"></span>
    <span style="width:34px;height:21px;border-radius:3px;background:#e8e8e8"></span>
    <span style="width:34px;height:21px;border-radius:3px;background:#e8e8e8"></span>
    <span style="width:34px;height:21px;border-radius:3px;background:#1e5fb5"></span>
  </div>
</footer>

</body>
</html>
```